NPG Job bank

Western Guild of Bracework Practitioners Needs a design for our orthodontist job bank.

We are in the process of redesigning our current job board. We would like to improve our current design, focusing on the landing page and possibly the search page. I have attached images of what we currently have in place right now.

The Landing page: Currently, I find the landing page too wordy, members get confused when using it, we need something that is easier for providers are seekers to use. Set up more user friendly. Maybe have a button for become provider and become seeker and then a modal pops up with process.. The final design for this page needs to be user friendly, organized and clean. If someone were coming to this page for the first time they would know how to become a provider.

The search page: I was thinking it would be best to have the search options on the left hand side opposed to how it is just in the middle now. all of the information currently shown on this page needs to be included. The search results need improvement on how they are displayed as well.

If you have any questions feel free to contact me.

Industry/Entity Type

Bank

Number of Pages Required

1 page

Colors
33a6d7
85cae6
0692cd

Requirements
Must have
• A Landing page that is well designed and that is made in the blue colors that are shown on the attached files of what our job bank currently looks like. I have also attached 3 photos that could be used for a masthead, but keep in mind these do not have to be used, you can use any photo you would like, these are just for your convenience.
Nice to have
• An improved search results page along with the Landing page

```html
<!DOCTYPE html>
<html lang="en">
<head>
<meta charset="utf-8">
<title>NPG Job Bank</title>
<link rel="stylesheet" href="https://fonts.googleapis.com/css2?family=Arimo:wght@400;700&family=Bebas+Neue&display=swap">
<style>
:root{
  --top-bar:#1d6aab;
  --top-bar-dark:#135b9a;
  --header:#1f98cc;
  --card:#1b89c7;
  --card-band:#0e5c9f;
  --stripe:#0e5a9c;
  --footer-bg:#f5f6f7;
  --link:#1a5a9c;
  --heading:#222;
  --muted:#666;
  --white:#fff;
  --pale:#bfe3f3;
}
*{margin:0;padding:0;box-sizing:border-box}
html,body{width:1200px;height:1170px;overflow:hidden;background:var(--footer-bg);font-family:"Arimo",Arial,sans-serif}
.page{position:relative;width:1200px;height:1170px}
a{text-decoration:none;color:inherit}

.top-bar{position:absolute;left:0;top:0;width:1200px;height:38px;background:var(--top-bar)}
.top-bar .account-zone{position:absolute;left:618px;top:0;width:530px;height:38px;background:var(--top-bar-dark)}
.utility-nav{position:absolute;left:113px;top:15px;display:flex;gap:16px;font-size:10px;font-weight:700;color:var(--pale)}
.benefits-select{position:absolute;left:417px;top:5px;width:119px;height:30px;background:#2d8dcf;border:1px solid #4aa3dc;border-radius:2px;color:var(--white);font-size:10px;font-weight:700;padding:10px 0 0 10px}
.benefits-select svg{position:absolute;right:9px;top:10px}
.account-links{position:absolute;left:694px;top:12px;font-size:12px;color:var(--white)}
.social{position:absolute;left:778px;top:11px;display:flex;gap:9px}
.social span{width:14px;height:14px;border-radius:50%;background:var(--white)}
.search{position:absolute;left:886px;top:7px;width:204px;height:24px;background:var(--white);border-radius:3px;font-size:11px;color:#9aa;padding:5px 0 0 8px}
.search svg{position:absolute;right:10px;top:5px}

.header{position:absolute;left:0;top:38px;width:1200px;height:117px;background:var(--header)}
.brand{position:absolute;left:113px;top:26px;display:flex;align-items:center;gap:10px}
.brand-square{width:52px;height:50px;background:var(--white);border-radius:4px}
.brand-name{font-size:14px;line-height:14px;color:#0e4f8c;width:90px}
.tagline{position:absolute;left:113px;top:85px;font-size:8px;color:#0e4f8c}
.main-nav{position:absolute;left:318px;top:51px;display:flex;gap:14px;font-size:13.5px;color:var(--white)}

.hero{position:absolute;left:0;top:155px;width:1200px;height:613px;background:linear-gradient(100deg,#7e8a93 0%,#c8cdd1 28%,#e7e9ea 50%,#d9dcde 70%,#9aa3aa 100%)}
.slide-marker{position:absolute;left:32px;top:540px;width:1px;height:73px;background:var(--white)}
.cta{position:absolute;top:380px;width:444px;height:154px;background:var(--card);border-radius:8px;overflow:hidden;text-align:center;color:var(--white)}
.cta .band{position:absolute;left:0;top:0}
.cta-icon{position:absolute;left:50%;top:26px;transform:translateX(-50%)}
.cta-title{position:absolute;left:0;right:0;top:72px;font-family:"Bebas Neue",Impact,sans-serif;font-size:37px;letter-spacing:.3px}
.cta-sub{position:absolute;left:0;right:0;top:117px;font-size:16.5px}
.cta.provider{left:127px}
.cta.seeker{left:633px}
.stripe{position:absolute;left:0;top:768px;width:1200px;height:12px;background:var(--stripe)}

.footer-col{position:absolute;top:820px;font-size:12.5px}
.footer-col h4{font-size:12.5px;color:var(--heading);margin-bottom:11px}
.footer-col a{display:block;color:var(--link);line-height:30px}
.footer-col.awards{top:815px}
.partners{position:absolute;left:800px;top:953px}
.partners div{position:absolute;border-radius:3px}
.legal{position:absolute;left:0;top:1110px;width:1200px;border-top:1px solid #dcdfe1;height:60px}
.legal-row{position:absolute;left:137px;top:24px;display:flex;font-size:12.5px;color:var(--muted)}
.legal-row span{padding:0 11px;border-left:1px solid #ccc}
.legal-row span:first-child{padding-left:0;border:none}
.legal-row .links{color:var(--link)}
</style>
</head>
<body>
<div class="page">
  <div class="top-bar">
    <nav class="utility-nav"><a>Home</a><a>Store</a><a>Contact</a><a>NPG Member Directory</a><a>About</a></nav>
    <div class="benefits-select">Benefits For
      <svg width="10" height="7" viewBox="0 0 10 7"><path d="M1 1l4 4 4-4" fill="none" stroke="#fff" stroke-width="1.8"/></svg>
    </div>
    <div class="account-zone"></div>
    <div class="account-links">join &nbsp;|&nbsp; sign in</div>
    <div class="social" aria-label="Social links"><span></span><span></span><span></span><span></span></div>
    <div class="search">search
      <svg width="14" height="14" viewBox="0 0 14 14"><circle cx="5.5" cy="5.5" r="4.3" fill="none" stroke="#1b89c7" stroke-width="2"/><path d="M8.7 8.7l4 4" stroke="#1b89c7" stroke-width="2.2"/></svg>
    </div>
  </div>

  <header class="header">
    <div class="brand"><div class="brand-square"></div><div class="brand-name">Western Guild of Bracework Practitioners</div></div>
    <div class="tagline">Bright Bite. Bright Day.</div>
    <nav class="main-nav"><a>Meetings &amp; Events</a><a>Education</a><a>Practice Management</a><a>News &amp; Publications</a><a>Library &amp; Research</a><a>Legal &amp; Advocacy</a><a>Communities</a></nav>
  </header>

  <section class="hero" role="img" aria-label="Orthodontists in white coats treating a smiling patient in a bright clinic">
    <div class="slide-marker"></div>
    <a class="cta provider">
      <svg class="band" width="444" height="40" viewBox="0 0 444 40"><path d="M0 0H444V24Q222 -4 0 24Z" fill="var(--card-band)"/></svg>
      <svg class="cta-icon" width="32" height="32" viewBox="0 0 32 32"><path d="M6 3h15l5 5v18H6z" fill="none" stroke="#fff" stroke-width="2"/><path d="M10 11h11M10 15h11M10 19h8" stroke="#fff" stroke-width="2"/><path d="M19 28l9-9 2 2-9 9h-2z" fill="#fff"/></svg>
      <div class="cta-title">Become Provider</div>
      <div class="cta-sub">POST AN OPPORTUNITY OR SEARCH RESUMES</div>
    </a>
    <a class="cta seeker">
      <svg class="band" width="444" height="40" viewBox="0 0 444 40"><path d="M0 0H444V24Q222 -4 0 24Z" fill="var(--card-band)"/></svg>
      <svg class="cta-icon" width="34" height="34" viewBox="0 0 34 34"><circle cx="14" cy="14" r="9.5" fill="none" stroke="#fff" stroke-width="3.5"/><path d="M21 21l9 9" stroke="#fff" stroke-width="5" stroke-linecap="round"/></svg>
      <div class="cta-title">Become Seeker</div>
      <div class="cta-sub">FIND AN OPPORTUNITY OR UPLOAD RESUME</div>
    </a>
  </section>
  <div class="stripe"></div>

  <footer>
    <div class="footer-col" style="left:157px"><h4>About NPG</h4><a>What We Do</a><a>Mission &amp; History</a><a>Governance</a><a>Financial Information</a><a>Strategic Plan</a></div>
    <div class="footer-col" style="left:317px;top:824px"><a>Awards</a><a>Advertise with Us</a><a>Calendar</a><a>Contact Us</a></div>
    <div class="footer-col" style="left:477px"><h4>Membership</h4><a>Join</a><a>Orthodontists</a><a>Students/Residents</a><a>Orthodontic Staff</a><a>International</a><a>International Students</a></div>
    <div class="footer-col" style="left:637px"><h4>Tools</h4><a>My NPG</a><a>NPG Communities</a><a>Member Directory</a><a>Webmail</a><a>CE Manager</a></div>
    <div class="footer-col" style="left:797px"><h4>NPG Sites</h4><a>NPG Foundation</a><a>brightbitehub.org</a><a>NPG Insurance Company</a></div>
    <div class="partners" aria-label="Partner sites">
      <div style="left:0;top:5px;width:106px;height:36px;background:#8cc63f"></div>
      <div style="left:118px;top:0;width:92px;height:44px;background:#2a8fd0"></div>
      <div style="left:5px;top:64px;width:92px;height:36px;background:#2a8fd0"></div>
      <div style="left:108px;top:56px;width:98px;height:50px;background:#1a5fa0"></div>
    </div>
    <div class="legal">
      <div class="legal-row">
        <span>© 2013 Western Guild of Bracework Practitioners</span>
        <span>218 Harbor Row, Lakemont, OR 97402</span>
        <span>(800) 555-0142 or (503) 555-0178</span>
        <span class="links">Terms of Use &nbsp; Privacy Policy</span>
      </div>
    </div>
  </footer>
</div>
</body>
</html>
```